Innovative Event Ticketing Start Up. Needs a Web Design

We need a web design for a new company based in London called 'Bandwick'. We are a platform which facilitates the building of groups of customers for events. As more people commit to an event, the price incrementally decreases. We would like there to be an emphasis on the sharing element and the decreasing price with higher participation.

Any quieres please email me at rlvo57@mailtrove.net

Target Market(s)

18-30 year olds who are active and savvy across social media sites

Industry/Entity Type

Events

Number of Pages Required

3 page

Font styles to use
Other font styles liked:
• Phi Roman

Requirements
Must have
• Each event offering runs for a limited time so a countdown timer is also to be included as well as a counter of number of participants (please find example attached).
• The interface needs to have the options for 'Live 'Music', 'Nightlife', 'Festivals', 'Comedy' and 'Everything Else'. Also
• A 'featured' section, for our promoted events
• Social sharing icons for Chatterbarn, Quillow, PingMesh, SMS and Email
• Room the inclusion of a video
• Pages for clients to sign up - registering details ect.
• Content is still being completed, so room available to add when ready
Nice to have
• An interface design we like as a guiding templates on is https://kumvoxapp.com/
• Zamo wordpress theme is also of interest.
• Scroll over clicking for main interface and also for the event once clicked upon.
• Event pages similar desgin to kumvox with same features such as Trelvo Charts but also participant counter and affiliate marketing options.
Should not have
• CMS no longer necessary

```html
<!DOCTYPE html>
<html lang="en">
<head>
<meta charset="utf-8">
<title>Bandwick</title>
<link href="https://fonts.googleapis.com/css2?family=Open+Sans:wght@400;600;700&family=Oswald:wght@500&display=swap" rel="stylesheet">
<style>
:root{
  --orange:#f05a1e;
  --orange-dark:#d94a12;
  --ink:#2b2b2b;
  --dark:#222222;
  --grey-text:#8a8a8a;
  --hero-bg:#dcdcdc;
  --white:#ffffff;
  --line:#e3e3e3;
}
*{box-sizing:border-box;margin:0;padding:0}
html,body{width:688px;height:1200px;overflow:hidden;background:var(--white)}
body{font-family:"Open Sans",Arial,sans-serif;color:var(--ink);position:relative}
.topbar{height:14px;background:var(--dark);display:flex;align-items:center;justify-content:space-between;padding:0 14px;font-size:7px;color:#ddd}
.topbar .social{display:flex;gap:5px}
.topbar .social span{width:6px;height:6px;border-radius:50%;background:#bbb;display:block}
.header{height:56px;display:flex;align-items:center;justify-content:space-between;padding:0 22px 0 16px;border-bottom:1px solid var(--line)}
.brand{display:flex;align-items:center;gap:8px}
.brand-mark{width:26px;height:26px;background:var(--orange);display:block}
.brand-name{font-family:"Oswald",sans-serif;font-size:20px;font-weight:500;color:var(--ink);letter-spacing:.5px}
.nav{display:flex;gap:22px;font-size:9px;color:#555}
.hero{height:188px;background:linear-gradient(#e6e6e6,var(--hero-bg));text-align:center;padding-top:18px}
.hero h1{font-weight:400;font-size:31px;color:var(--orange);line-height:1.1}
.hero p{font-size:7.5px;color:#666;width:440px;margin:8px auto 0;line-height:1.45}
.countdown{display:flex;justify-content:center;align-items:flex-start;gap:6px;margin-top:12px}
.unit{display:flex;flex-direction:column;align-items:center}
.unit b{width:42px;height:42px;background:#333;color:var(--white);font-size:24px;font-weight:700;display:flex;align-items:center;justify-content:center;border-radius:3px}
.unit small{font-size:8px;font-weight:700;margin-top:4px;color:var(--ink)}
.sep{font-size:22px;font-weight:700;line-height:42px;color:#444}
.btn-outline{display:inline-block;margin-top:8px;border:1.5px solid #444;background:var(--white);font-size:10px;padding:5px 14px;color:var(--ink);border-radius:2px}
.band{height:40px;background:var(--orange);display:flex;align-items:center;justify-content:space-between;padding:0 42px 0 38px}
.band p{font-size:7px;color:#fde2d4;width:380px;line-height:1.4}
.btn-dark{background:var(--dark);color:var(--white);font-size:10px;font-weight:600;padding:6px 14px;border-radius:2px}
.categories{display:flex;justify-content:center;gap:14px;padding-top:26px}
.card{width:120px;text-align:center}
.card h3{font-size:13px;font-weight:700;margin-bottom:6px}
.card .photo{height:68px;border-radius:2px}
.card p{font-size:6.5px;color:#555;text-align:left;padding:9px 12px 6px;line-height:1.4}
.btn-orange{display:inline-block;background:var(--orange);color:var(--white);font-size:7px;padding:3px 9px;border-radius:2px}
.card .body{box-shadow:0 2px 5px rgba(0,0,0,.15);padding-bottom:8px}
.pager{display:flex;justify-content:center;gap:6px;margin-top:12px;font-size:8px;color:#888;align-items:center}
.pager i{width:5px;height:5px;border-radius:50%;background:#bbb;display:block;font-style:normal}
.intro{text-align:center;padding-top:24px}
.intro h2{font-size:15.5px;font-weight:400;color:var(--orange)}
.intro .rule{width:440px;height:1px;background:var(--line);margin:8px auto 10px}
.intro p{width:550px;margin:0 auto;font-size:7.5px;color:#888;line-height:1.5}
.intro .btn-outline{margin-top:12px;font-size:10px}
.featured{position:absolute;top:752px;left:0;width:688px;height:392px;background:var(--orange);padding-top:16px}
.featured h2{text-align:center;color:var(--white);font-weight:400;font-size:17px}
.featured .rule{width:200px;height:1px;background:rgba(255,255,255,.5);margin:8px auto 14px}
.event{width:550px;height:62px;margin:0 auto 11px;background:linear-gradient(#3a3a3a,#1f1f1f);border-radius:31px;display:flex;align-items:center;padding-left:6px}
.event svg{flex:none}
.event .count{font-size:14px;font-weight:700;color:var(--white);width:150px;padding-left:16px}
.event p{font-size:7px;color:#ddd;line-height:1.5;width:320px}
.event p em{font-style:normal;color:var(--orange)}
.footer{position:absolute;bottom:0;left:0;width:688px;height:30px;background:var(--dark);display:flex;align-items:center;justify-content:space-between;padding:0 22px;font-size:8px;color:#ccc}
.footer nav{display:flex;gap:26px}
</style>
</head>
<body>
<div class="topbar">
  <span>&#9632; Sign Up</span>
  <div class="social"><span></span><span></span><span></span><span></span><span></span></div>
</div>
<header class="header">
  <div class="brand"><span class="brand-mark"></span><span class="brand-name">BANDWICK</span></div>
  <nav class="nav"><span>Home</span><span>About</span><span>Events</span><span>Schedule</span><span>Participants</span><span>Contact Us</span></nav>
</header>
<section class="hero">
  <h1>Get Ready for the Next Event!</h1>
  <p>Our platform groups fans together for live events. The more people who commit, the lower the ticket price drops for everyone in the crowd, so bring friends.</p>
  <div class="countdown">
    <div class="unit"><b>3</b><small>MONTHS</small></div><span class="sep">:</span>
    <div class="unit"><b>40</b><small>DAYS</small></div><span class="sep">:</span>
    <div class="unit"><b>59</b><small>HOURS</small></div>
  </div>
  <span class="btn-outline">Register Now</span>
</section>
<section class="band">
  <p>Join a crowd, share the event and watch the price fall. Every new participant brings the ticket cost down a little further for all of you.</p>
  <span class="btn-dark">Watch Video</span>
</section>
<section class="categories">
  <div class="card"><h3>Live 'Music</h3><div class="body"><div class="photo" role="img" aria-label="Live music concert photo" style="background:linear-gradient(135deg,#6b6b6b,#1e1e1e)"></div><p>Gather your group early and the ticket price drops as more fans sign up to join.</p><span class="btn-orange">Register Now</span></div></div>
  <div class="card"><h3>Nightlife</h3><div class="body"><div class="photo" role="img" aria-label="Nightclub crowd photo" style="background:linear-gradient(135deg,#5a5f7a,#2b1f33)"></div><p>Gather your group early and the ticket price drops as more fans sign up to join.</p><span class="btn-orange">Register Now</span></div></div>
  <div class="card"><h3>Festivals</h3><div class="body"><div class="photo" role="img" aria-label="Outdoor festival crowd photo" style="background:linear-gradient(135deg,#c9c9c9,#4d4d4d)"></div><p>Gather your group early and the ticket price drops as more fans sign up to join.</p><span class="btn-orange">Register Now</span></div></div>
  <div class="card"><h3>Comedy</h3><div class="body"><div class="photo" role="img" aria-label="Comedy show photo" style="background:linear-gradient(135deg,#e0dcd8,#8a7f76)"></div><p>Gather your group early and the ticket price drops as more fans sign up to join.</p><span class="btn-orange">Register Now</span></div></div>
</section>
<div class="pager"><span>&#9664;</span><i></i><i></i><span>&#9654;</span></div>
<section class="intro">
  <h2>Lorem Ipsum is simply dummy text of the printing and typesetting</h2>
  <div class="rule"></div>
  <p>Bandwick brings people together for the events they love. Pick a show, share it with friends across your social feeds and see the price fall as the group grows. Each offer runs for a limited time, so the countdown keeps everyone moving and the best deals go to the crowds that commit early.</p>
  <span class="btn-outline">Read More</span>
</section>
<section class="featured">
  <h2>Featured Promoted Events</h2>
  <div class="rule"></div>
  <div class="event"><svg width="52" height="52" viewBox="0 0 52 52"><circle cx="26" cy="26" r="24" fill="none" stroke="#555" stroke-width="3"/><path d="M26 2 A24 24 0 1 1 5 37" fill="none" stroke="#f05a1e" stroke-width="3"/><circle cx="26" cy="26" r="15" fill="#f05a1e"/><text x="26" y="25" text-anchor="middle" font-size="9" font-weight="700" fill="#fff" font-family="Open Sans,sans-serif">15</text><text x="26" y="33" text-anchor="middle" font-size="6" fill="#fff" font-family="Open Sans,sans-serif">Days</text></svg><span class="count">100 participants</span><p>A featured event promoted by our partners. Join now to lock in your place, share it with friends and drive the price down before the clock runs out. <em>Read More</em></p></div>
  <div class="event"><svg width="52" height="52" viewBox="0 0 52 52"><circle cx="26" cy="26" r="24" fill="none" stroke="#555" stroke-width="3"/><path d="M26 2 A24 24 0 1 1 5 37" fill="none" stroke="#f05a1e" stroke-width="3"/><circle cx="26" cy="26" r="15" fill="#f05a1e"/><text x="26" y="25" text-anchor="middle" font-size="9" font-weight="700" fill="#fff" font-family="Open Sans,sans-serif">15</text><text x="26" y="33" text-anchor="middle" font-size="6" fill="#fff" font-family="Open Sans,sans-serif">Days</text></svg><span class="count">100 participants</span><p>A featured event promoted by our partners. Join now to lock in your place, share it with friends and drive the price down before the clock runs out. <em>Read More</em></p></div>
  <div class="event"><svg width="52" height="52" viewBox="0 0 52 52"><circle cx="26" cy="26" r="24" fill="none" stroke="#555" stroke-width="3"/><path d="M26 2 A24 24 0 1 1 5 37" fill="none" stroke="#f05a1e" stroke-width="3"/><circle cx="26" cy="26" r="15" fill="#f05a1e"/><text x="26" y="25" text-anchor="middle" font-size="9" font-weight="700" fill="#fff" font-family="Open Sans,sans-serif">15</text><text x="26" y="33" text-anchor="middle" font-size="6" fill="#fff" font-family="Open Sans,sans-serif">Days</text></svg><span class="count">100 participants</span><p>A featured event promoted by our partners. Join now to lock in your place, share it with friends and drive the price down before the clock runs out. <em>Read More</em></p></div>
  <div class="event"><svg width="52" height="52" viewBox="0 0 52 52"><circle cx="26" cy="26" r="24" fill="none" stroke="#555" stroke-width="3"/><path d="M26 2 A24 24 0 1 1 5 37" fill="none" stroke="#f05a1e" stroke-width="3"/><circle cx="26" cy="26" r="15" fill="#f05a1e"/><text x="26" y="25" text-anchor="middle" font-size="9" font-weight="700" fill="#fff" font-family="Open Sans,sans-serif">15</text><text x="26" y="33" text-anchor="middle" font-size="6" fill="#fff" font-family="Open Sans,sans-serif">Days</text></svg><span class="count">100 participants</span><p>A featured event promoted by our partners. Join now to lock in your place, share it with friends and drive the price down before the clock runs out. <em>Read More</em></p></div>
</section>
<footer class="footer">
  <nav><span>Home</span><span>About</span><span>Events</span><span>Schedule</span><span>Participants</span><span>Contact Us</span></nav>
  <span>Bandwick Copyright 2015</span>
</footer>
</body>
</html>
```